New website

Our website (www.larchvale.com) needs to be replaced with something gorgeous and glossy. We do like the text of our current website but have many new images to put on the site. We want to create a website that shows viewers what our team can do, and how we can create something amazing for them and their homes.

Coding

```html
<!DOCTYPE html>
<html lang="en">
<head>
<meta charset="utf-8">
<title>Larchvale Landscaping</title>
<link href="https://fonts.googleapis.com/css2?family=Cinzel:wght@400;600;700&family=Merriweather:ital,wght@0,300;0,400;0,700;1,400&display=swap" rel="stylesheet">
<style>
:root{
  --green:#3daf4f;
  --green-dark:#2e8f3e;
  --blue:#2a6bb5;
  --blue-light:#7fb2e3;
  --ink:#222;
  --text:#555;
  --grey-band:#f3f3f3;
  --footer:#1b1d20;
  --white:#fff;
}
*{box-sizing:border-box;margin:0;padding:0}
html,body{width:1200px;height:4178px;overflow:hidden}
body{position:relative;background:var(--white);font-family:'Merriweather',serif;color:var(--text)}
.abs{position:absolute}
.heading{font-family:'Cinzel',serif;font-weight:700;color:var(--ink);text-align:center;font-size:44px;letter-spacing:1px}
.heading-bar{width:64px;height:4px;background:var(--blue);margin:14px auto 0}
.btn{position:absolute;background:var(--green);color:#fff;font-family:'Cinzel',serif;font-weight:700;font-size:14px;display:flex;align-items:center;justify-content:center;border-radius:4px}

/* header */
.site-header{top:0;left:0;width:1200px;height:96px;background:#fff}
.brand{left:97px;top:26px;font-family:'Cinzel',serif;font-weight:400;color:#333;font-size:30px;letter-spacing:5px}
.brand-sub{left:140px;top:62px;font-family:'Cinzel',serif;font-size:8px;letter-spacing:9px;color:#333}
.nav{left:384px;top:40px;display:flex;gap:19px;font-family:'Cinzel',serif;font-weight:700;font-size:14px;color:#333}
.nav .active{color:var(--green);border-bottom:2px solid var(--green)}
.nav-cta{left:890px;top:20px;width:206px;height:56px}

/* hero */
.hero{top:96px;left:0;width:1200px;height:545px;background:linear-gradient(110deg,#1c3a16 0%,#2f5a22 40%,#4a7d2d 70%,#6b8f4a 100%)}
.hero-kicker{left:97px;top:200px;font-family:'Cinzel',serif;color:#fff;font-size:21px;letter-spacing:3px}
.hero-title{left:97px;top:240px;font-family:'Cinzel',serif;font-weight:700;color:#fff;font-size:72px;letter-spacing:7px}
.hero-sub{left:97px;top:325px;font-family:'Cinzel',serif;color:#fff;font-size:42px;letter-spacing:12px}
.hero-btn{left:97px;top:400px;width:262px;height:54px;background:#fff;color:#222;border-radius:6px}
.dots{left:580px;top:542px;display:flex;gap:6px}
.dots span{width:7px;height:7px;border-radius:50%;background:#fff}
.dots span.on{background:var(--blue-light);width:9px;height:9px;margin-top:-1px}

/* services */
.card{position:absolute;width:334px;height:338px;border-left:4px solid var(--green);background:#fff}
.card .photo{width:100%;height:256px}
.card .label{position:absolute;left:18px;top:284px;font-family:'Merriweather',serif;font-weight:700;color:#333;font-size:19px;line-height:26px}
.card .arrow{position:absolute;right:50px;top:282px}

/* why */
.why{top:1737px;left:0;width:1200px;height:351px;background:var(--grey-band)}
.why-item{position:absolute;top:1893px;width:193px;height:193px;text-align:center;font-size:15px;color:#333}
.why-item .ic{width:76px;height:76px;margin:26px auto 18px;border-radius:50%;background:#fff;border:3px solid #ddd;display:flex;align-items:center;justify-content:center}
.why-item.active{background:var(--green);color:#fff}
.why-item.active .ic{border-color:#fff}

/* about */
.about-photo{left:112px;top:2177px;width:432px;height:446px;border-radius:0 80px 0 80px;background:linear-gradient(180deg,#7b6a73 0%,#8a5a3e 45%,#6b3f25 70%,#4e6b33 100%)}
.about-title{left:600px;top:2210px;font-family:'Cinzel',serif;font-weight:700;font-size:42px;color:#222}
.about-bar{left:600px;top:2266px;width:60px;height:4px;background:var(--blue)}
.about-text{left:600px;top:2300px;width:480px;font-size:15.5px;line-height:27px;color:#666}

/* portfolio */
.portfolio-band{top:2706px;left:0;width:1200px;height:374px;background:var(--green)}
.portfolio-title{top:2790px;left:0;width:1200px;color:#fff}
.pf{position:absolute;top:2903px;width:240px;height:308px;border-radius:14px}

/* testimonials */
.tcard{position:absolute;top:3406px;width:478px;height:203px;border-radius:100px 0 100px 0;display:flex;align-items:center}
.tcard .avatar{width:186px;height:186px;border-radius:50%;margin-left:8px;flex:none}
.tcard .body{margin-left:24px;margin-right:24px}
.tcard .quote{font-style:italic;font-size:17px;line-height:25px}
.tcard .name{font-family:'Cinzel',serif;font-size:20px;margin-top:14px}
.tcard .place{font-family:'Cinzel',serif;font-size:11px}
.round-arrow{position:absolute;top:3478px;width:44px;height:44px;border-radius:50%;display:flex;align-items:center;justify-content:center}

/* footer */
.footer{top:3779px;left:0;width:1200px;height:399px;background:var(--footer);color:#ddd}
.f-head{font-family:'Cinzel',serif;font-weight:700;font-size:21px;color:#fff}
.f-links{font-family:'Cinzel',serif;font-weight:700;font-size:14px;color:#fff;line-height:40px}
.f-row{display:flex;gap:14px;margin-bottom:14px;font-size:14.5px;line-height:22px;color:#fff}
.f-ic{width:38px;height:38px;border-radius:50%;background:var(--green);flex:none;display:flex;align-items:center;justify-content:center}
.social{width:46px;height:46px;border-radius:50%;border:2px solid #fff}
</style>
</head>
<body>

<header class="abs site-header">
  <div class="abs brand">LARCHVALE</div>
  <div class="abs brand-sub">LANDSCAPING</div>
  <nav class="abs nav"><span class="active">HOME</span><span>ABOUT US</span><span>SERVICES</span><span>TESTIMONIALS</span><span>CONTACT US</span></nav>
  <div class="btn nav-cta">MAKE AN APOINTMENT</div>
</header>

<section class="abs hero" role="img" aria-label="Lush green lawn with a curving stone path and garden steps"></section>
<div class="abs hero-kicker">WELCOME TO</div>
<div class="abs hero-title">LARCHVALE</div>
<div class="abs hero-sub">LANDSCAPING</div>
<div class="btn hero-btn">SCHEDULE AN APPOINTMENT</div>
<div class="abs dots"><span></span><span class="on"></span><span></span></div>
<svg class="abs" style="left:0;top:540px" width="1200" height="110" viewBox="0 0 1200 110">
  <path d="M0 40 C300 120 700 20 1200 40 L1200 110 L0 110Z" fill="#fff"/>
  <path d="M40 52 C350 110 800 20 1200 50 L1200 60 C800 35 380 130 40 52Z" fill="var(--blue)"/>
  <path d="M0 36 C250 90 600 40 1200 30 L1200 40 C700 40 300 110 0 44Z" fill="#fff"/>
</svg>

<!-- services -->
<div class="abs" style="top:713px;left:0;width:1200px">
  <h2 class="heading">OUR SERVICES</h2><div class="heading-bar"></div>
</div>
<svg width="0" height="0" style="position:absolute"><defs>
  <symbol id="arrow" viewBox="0 0 36 16"><path d="M0 8H33M26 1L34 8L26 15" fill="none" stroke="#222" stroke-width="2.5"/></symbol>
</defs></svg>

<div class="card" style="left:97px;top:830px"><div class="photo" role="img" aria-label="Worker starting a lawn mower" style="background:linear-gradient(135deg,#4f7a2a,#a23a2b 50%,#d08a1a)"></div><div class="label">LAWN<br>MAINTENANCE</div><svg class="arrow" width="36" height="16"><use href="#arrow"/></svg></div>
<div class="card" style="left:431px;top:830px"><div class="photo" role="img" aria-label="Gardener trimming hedges" style="background:linear-gradient(135deg,#5c8a2c,#d07a2a 45%,#3c6a20)"></div><div class="label">LANDSCAPE<br>MAINTENANCE</div><svg class="arrow" width="36" height="16"><use href="#arrow"/></svg></div>
<div class="card" style="left:765px;top:830px"><div class="photo" role="img" aria-label="Laying a roll of fresh sod" style="background:linear-gradient(135deg,#6a5a45,#5b8a34 55%,#4b3a2a)"></div><div class="label">LANDSCAPING</div><svg class="arrow" width="36" height="16"><use href="#arrow"/></svg></div>

<div class="card" style="left:97px;top:1215px"><div class="photo" role="img" aria-label="Spreading fertilizer across a lawn" style="background:linear-gradient(135deg,#7d9a5a,#4f7a2c 60%,#2e3a2a)"></div><div class="label">LAWN<br>FERTILIZATION</div><svg class="arrow" width="36" height="16"><use href="#arrow"/></svg></div>
<div class="card" style="left:431px;top:1215px"><div class="photo" role="img" aria-label="Crew installing paving and mulch beds" style="background:linear-gradient(135deg,#6b6f5a,#9a9a8e 50%,#7a6a4a)"></div><div class="label">MULCH/BARK<br>INSTALLATION</div><svg class="arrow" width="36" height="16"><use href="#arrow"/></svg></div>
<div class="card" style="left:765px;top:1215px"><div class="photo" role="img" aria-label="Trimming a shrub with hedge shears" style="background:linear-gradient(135deg,#5a7a3a,#3a6a22 60%,#2e5a1e)"></div><div class="label">TREE SERVICES<br>&amp; SHRUB PRUNING</div><svg class="arrow" width="36" height="16"><use href="#arrow"/></svg></div>

<div class="btn" style="left:512px;top:1591px;width:177px;height:55px">VIEW ALL SERVICES</div>

<!-- why -->
<section class="abs why"></section>
<div class="abs" style="top:1782px;left:0;width:1200px">
  <h2 class="heading">WHY CHOOSE US?</h2><div class="heading-bar"></div>
</div>
<div class="why-item" style="left:80px"><div class="ic"><svg width="40" height="40" viewBox="0 0 40 40"><circle cx="20" cy="16" r="11" fill="none" stroke="#555" stroke-width="2"/><path d="M13 25L10 37L20 32L30 37L27 25" fill="none" stroke="#555" stroke-width="2"/></svg></div>Specialized Company</div>
<div class="why-item active" style="left:315px"><div class="ic"><svg width="40" height="40" viewBox="0 0 40 40"><circle cx="20" cy="20" r="14" fill="none" stroke="#555" stroke-width="2"/><path d="M13 20L18 25L27 15" fill="none" stroke="#555" stroke-width="2.5"/></svg></div>Dependable Services<br><svg width="28" height="14" viewBox="0 0 36 16" style="margin-top:6px"><path d="M0 8H33M26 1L34 8L26 15" fill="none" stroke="#fff" stroke-width="2.5"/></svg></div>
<div class="why-item" style="left:528px"><div class="ic"><svg width="40" height="40" viewBox="0 0 40 40"><rect x="7" y="9" width="26" height="24" rx="2" fill="none" stroke="#555" stroke-width="2"/><path d="M7 16H33M13 5V12M27 5V12" stroke="#555" stroke-width="2"/></svg></div>Day Scheduling</div>
<div class="why-item" style="left:713px"><div class="ic"><svg width="40" height="40" viewBox="0 0 40 40"><rect x="6" y="8" width="28" height="18" rx="3" fill="none" stroke="#555" stroke-width="2"/><path d="M14 26L12 33L20 26" fill="none" stroke="#555" stroke-width="2"/></svg></div>Free Consultations</div>
<div class="why-item" style="left:919px"><div class="ic"><svg width="40" height="40" viewBox="0 0 40 40"><path d="M20 6L24 15L34 16L26 22L29 32L20 27L11 32L14 22L6 16L16 15Z" fill="none" stroke="#555" stroke-width="2"/></svg></div>top rated landscapers</div>

<!-- about -->
<div class="abs about-photo" role="img" aria-label="Large timber home with a lawn at dusk"></div>
<h2 class="abs about-title">ABOUT US</h2>
<div class="abs about-bar"></div>
<p class="abs about-text">Established in 2005 as a way to pay for college tuition, Larchvale has instead become our passion. With a garage sale mower and a commitment to doing every job well, our list of satisfied customers grew quickly over the years.While the scope of our landscaping company has grown, our way of doing business has not. It is still rooted in the desire to do quality work whether the job includes a simple tree service or the installation</p>
<div class="btn" style="left:600px;top:2507px;width:130px;height:56px">LEARN MORE</div>

<!-- portfolio -->
<section class="abs portfolio-band"></section>
<div class="abs portfolio-title">
  <h2 class="heading" style="color:#fff">OUR PORTFOLIO</h2><div class="heading-bar" style="background:#fff"></div>
</div>
<div class="pf" style="left:-14px;border-radius:0 14px 14px 0;background:linear-gradient(180deg,#b7c3cf,#8a8a80 45%,#4f8a30 75%,#3a6a22)" role="img" aria-label="Suburban house with a manicured front lawn"></div>
<div class="pf" style="left:239px;background:linear-gradient(180deg,#c88a9a,#8a6a5a 45%,#d8d8d0 75%,#5a7a3a)" role="img" aria-label="Modern home with a stone walkway at sunset"></div>
<div class="pf" style="left:492px;background:linear-gradient(180deg,#8aa0b0,#6b6a60 45%,#4f7a30 80%)" role="img" aria-label="Stone-fronted home with landscaped yard"></div>
<div class="abs" style="left:492px;top:3013px;width:240px;text-align:center;font-family:'Cinzel',serif;color:#fff;font-size:22px;letter-spacing:4px">LARCHVALE</div>
<div class="btn" style="left:539px;top:3048px;width:144px;height:48px">VIEW DETAILS</div>
<div class="pf" style="left:742px;background:linear-gradient(135deg,#3a6a22,#8aa24a 40%,#c8b89a 60%,#9a9a9a)" role="img" aria-label="Decorative river rock and turf border"></div>
<div class="pf" style="left:994px;width:220px;border-radius:14px 0 0 14px;background:linear-gradient(135deg,#4a7a3a,#3aa8c8 40%,#6a5a4a 70%,#4a4a4a)" role="img" aria-label="Landscaper planting in a garden bed"></div>

<!-- testimonials -->
<div class="abs" style="top:3290px;left:0;width:1200px">
  <h2 class="heading">OUR CLIENT TESTIMONIALS</h2><div class="heading-bar"></div>
</div>
<div class="round-arrow" style="left:24px;border:2px solid #333"><svg width="12" height="14"><path d="M9 1L3 7L9 13" fill="none" stroke="#333" stroke-width="2"/></svg></div>
<div class="round-arrow" style="left:1122px;background:#111"><svg width="12" height="14"><path d="M3 1L9 7L3 13" fill="none" stroke="#fff" stroke-width="2"/></svg></div>

<div class="tcard" style="left:107px;background:#fff;border:2px solid #ddd;box-shadow:0 8px 20px rgba(0,0,0,.08)">
  <div class="avatar" role="img" aria-label="Portrait of a smiling client in a garden" style="background:linear-gradient(135deg,#8aa25a,#3a4a3a)"></div>
  <div class="body" style="color:#444"><div class="quote">"We are delighted to have Larchvale's quality service for another year. Thanks!"</div><div class="name" style="color:#222">Dorian P.</div><div class="place">North Ridge Hollow</div></div>
</div>
<div class="tcard" style="left:616px;background:var(--green);box-shadow:0 8px 20px rgba(0,0,0,.12)">
  <div class="avatar" role="img" aria-label="Portrait of a smiling client in a blue shirt" style="background:linear-gradient(135deg,#b8a78a,#2f6bb0)"></div>
  <div class="body" style="color:#fff"><div class="quote">"The landscape you installed in my front yard looks fantastic! Thanks so much!"</div><div class="name">Marsh, Ivy</div></div>
</div>

<!-- footer -->
<svg class="abs" style="left:0;top:3690px" width="1200" height="100" viewBox="0 0 1200 100" preserveAspectRatio="none">
  <path d="M0 40 C300 90 700 -10 1200 30 L1200 100 L0 100Z" fill="var(--blue)"/>
  <path d="M0 60 C350 110 750 10 1200 42 L1200 100 L0 100Z" fill="var(--footer)"/>
</svg>
<footer class="abs footer">
  <div class="abs" style="left:97px;top:114px;font-family:'Cinzel',serif;font-size:30px;letter-spacing:5px;color:#fff">LARCHVALE</div>
  <div class="abs" style="left:140px;top:150px;font-family:'Cinzel',serif;font-size:8px;letter-spacing:9px;color:#fff">LANDSCAPING</div>
  <p class="abs" style="left:97px;top:178px;width:280px;font-size:13.5px;line-height:22px;color:#fff">Lorem ipsum dolor sit amet, consectetur adipiscing elit, sed do eiusmod tempor incididunt ut labore et dolore magna aliqua. Quis ipsum suspendisse ultrices gravida. Risus</p>

  <div class="abs" style="left:448px;top:80px"><div class="f-head">Quick Links</div>
    <div class="f-links" style="margin-top:12px">HOME<br>ABOUT US<br>SERVICES<br>TESTIMONIALS<br>CONTACT US</div></div>

  <div class="abs" style="left:650px;top:78px;width:270px"><div class="f-head" style="margin-bottom:18px">Contact Us</div>
    <div class="f-row"><div class="f-ic"><svg width="18" height="18" viewBox="0 0 24 24"><path d="M6 2L10 6L8 9C9 12 12 15 15 16L18 14L22 18L19 22C10 21 3 14 2 5Z" fill="#fff"/></svg></div><div>PHONE NO :<br>(555) 284-7160</div></div>
    <div class="f-row"><div class="f-ic"><svg width="16" height="20" viewBox="0 0 16 22"><path d="M8 0C3.6 0 0 3.4 0 7.8C0 13 8 22 8 22S16 13 16 7.8C16 3.4 12.4 0 8 0Z" fill="#fff"/><circle cx="8" cy="8" r="3" fill="var(--green)"/></svg></div><div>LOCATION :<br>1870 Willowbend Rd<br>SE Fernbrook, MI 49000</div></div>
    <div class="f-row"><div class="f-ic"><svg width="22" height="22" viewBox="0 0 24 24"><circle cx="12" cy="12" r="9" fill="none" stroke="#fff" stroke-width="2"/><path d="M12 7V12L15 14" stroke="#fff" stroke-width="2" fill="none"/></svg></div><div>BUSINESS HOURS<br>Monday-Saturday: 7:00am<br>-7:00pm Closed Sunday</div></div>
  </div>

  <div class="abs" style="left:931px;top:78px"><div class="f-head">Follow Us</div>
    <div style="display:flex;gap:16px;margin-top:18px">
      <div class="social" style="background:var(--green)" role="img" aria-label="Social profile"></div>
      <div class="social" role="img" aria-label="Social profile"></div>
      <div class="social" role="img" aria-label="Social profile"></div>
    </div></div>

  <div class="abs" style="left:148px;top:345px;width:905px;height:1px;background:#3a3d42"></div>
  <div class="abs" style="left:0;top:360px;width:1200px;text-align:center;font-size:13.5px;color:#fff">©2025 Larchvale Landscaping - All rights reserved.</div>
</footer>

</body>
</html>
```